Whitby's Yard & Garden Center Business Card Update

I need an updated Business card design for my Lawn and Garden Center. We do Landscaping installs, Lawn Mowing, Snow Removal and also have a Garden Center Retail Division. I uploaded a few of our previous business cards to give an idea of what we are starting with. The main goal of this update is to simplify and modernize the business card, not all of the services that are on the previous cards has to be on the new one but I would still like to highlight our main services. There is also a sample of our logo that Can be used in the design.

Industry/Entity Type

Landscaping

Contact Information for Business Card

Desmond Whitby
Desmond@Whitbysyardandgarden.example
Business (555) 208-7316
Cell (555) 391-6842

Colors

Designer to choose colors to be used in the design.

Requirements
Must have
• Services Provided :
• Landscaping
• Lawn Maintenance
• Snow Removal
• Garden Center

```html
<!DOCTYPE html>
<html lang="en">
<head>
<meta charset="utf-8">
<title>Whitby's Yard &amp; Garden Center – Business Card</title>
<link rel="stylesheet" href="https://fonts.googleapis.com/css2?family=Russo+One&family=Montserrat:wght@600;700&family=Nunito+Sans:wght@400;600&display=swap">
<style>
  :root {
    --bg: #2b2b2e;
    --navy-deep: #1c1858;
    --navy-light: #2b2c80;
    --gold: #ecd9a0;
    --gold-muted: #b9ab86;
    --leaf: #2f5a2c;
  }
  * { box-sizing: border-box; margin: 0; padding: 0; }
  html, body { width: 1200px; height: 780px; overflow: hidden; }
  body {
    background: var(--bg);
    display: flex;
    justify-content: center;
    align-items: center;
    gap: 90px;
  }
  .card {
    position: relative;
    width: 380px;
    height: 665px;
    background: linear-gradient(200deg, var(--navy-light) 0%, var(--navy-deep) 100%);
    box-shadow: 0 14px 30px rgba(0,0,0,.45);
    color: var(--gold);
    overflow: hidden;
  }
  .edge-band {
    position: absolute;
    left: 0; right: 0;
    height: 10px;
    background: var(--gold);
  }
  .card--back .edge-band { top: 0; }
  .card--front .edge-band { bottom: 0; }

  .brand {
    display: flex;
    align-items: center;
    justify-content: center;
    gap: 12px;
  }
  .brand__dot {
    width: 34px; height: 34px;
    border-radius: 50%;
    background: var(--leaf);
  }
  .brand__name {
    font-family: "Montserrat", sans-serif;
    font-weight: 700;
    font-size: 40px;
    color: var(--gold);
  }
  .card--back .brand {
    position: absolute;
    top: 250px; left: 0; right: 0;
  }
  .services {
    position: absolute;
    bottom: 40px; left: 0; right: 0;
    text-align: center;
    font-family: "Montserrat", sans-serif;
    font-weight: 700;
    font-size: 14.5px;
    letter-spacing: 1.6px;
    line-height: 1.45;
  }

  .card--front .brand {
    position: absolute;
    top: 70px; left: 0; right: 0;
  }
  .details {
    position: absolute;
    top: 215px; left: 40px; right: 30px;
  }
  .person__name {
    font-family: "Russo One", sans-serif;
    font-size: 31px;
    letter-spacing: 1px;
    line-height: 1;
  }
  .person__rule {
    width: 220px;
    height: 2px;
    background: var(--gold);
    margin: 14px 0 10px 22px;
  }
  .person__title {
    font-family: "Nunito Sans", sans-serif;
    font-weight: 600;
    font-size: 15px;
    letter-spacing: 1.4px;
  }
  .contact {
    list-style: none;
    margin-top: 40px;
    font-family: "Nunito Sans", sans-serif;
    font-size: 15px;
    line-height: 1.45;
  }
  .contact--web { margin-top: 22px; }
  .contact__label {
    display: inline-block;
    width: 72px;
    color: var(--gold-muted);
  }
  .company {
    margin-top: 36px;
    font-family: "Nunito Sans", sans-serif;
    font-weight: 600;
    font-size: 14.5px;
    letter-spacing: 1.4px;
  }
  .address {
    margin-top: 14px;
    font-family: "Nunito Sans", sans-serif;
    font-style: normal;
    font-size: 14.5px;
    letter-spacing: 1.2px;
    line-height: 1.4;
    color: var(--gold-muted);
  }
</style>
</head>
<body>
  <section class="card card--back" aria-label="Card back">
    <div class="edge-band"></div>
    <div class="brand">
      <span class="brand__dot"></span>
      <span class="brand__name">Whitby's</span>
    </div>
    <p class="services">LANDSCAPING-LAWN MAINTENANCE<br>SNOW REMOVAL-GARDEN CENTER</p>
  </section>

  <section class="card card--front" aria-label="Card front">
    <div class="brand">
      <span class="brand__dot"></span>
      <span class="brand__name">Whitby's</span>
    </div>
    <div class="details">
      <h1 class="person__name">DESMOND WHITBY</h1>
      <div class="person__rule"></div>
      <p class="person__title">CHIEF EXECUTIVE OFFICER</p>
      <ul class="contact contact--phone">
        <li><span class="contact__label">Business</span>(555) 208-7316</li>
        <li><span class="contact__label">Cell</span>(555) 391-6842</li>
      </ul>
      <ul class="contact contact--web">
        <li>www.whitbysyardandgarden.example</li>
        <li>Desmond@Whitbysyardandgarden.example</li>
      </ul>
      <p class="company">WHITBY'S YARD &amp; GARDEN CENTER</p>
      <address class="address">48 MEADOWBROOK LANE<br>FAIRHOLLOW, OH 45999</address>
    </div>
    <div class="edge-band"></div>
  </section>
</body>
</html>
```